Velmora Trade Hall (front page)

We need a design of a front page for our Velmora Trade Hall website (vth.co.uk). Our company is based in the United Kingdom and offers investors from all over the world an opportunity to invest into bitcoin and litecoin.

We have been developing this cutting edge technology for past 2 years based on our in depth knowledge on conventional stock and currency trading technology and methodology. We have run many test against penetration, security and stability and now are ready to deploy.

Recent news about vulnerability of such platforms leave a great deal of unease from retail investors about investing into cryptocurrency. We are set to challenge this attitude. Our background is payments in particular regulated environment in the UK. We are keen to apply our wealth of experience to provide secure and reliable trading platform and advance cryptocurrency as means of legal tender.

The front page should be based on the feel and look of our current technology vth.co.uk. Some of you have already been involved in logo design for our company, please see the attached mockups. The page should have this minimalist design, very clean and light.

Seek inspiration form www.korvelin.net, www.trusmarq.com, vip.plomwerth.com and other bitcoin exchanges.

We look forward to receiving your ideas.

You can also refer to our social pages:
https://www.facebook.com/vth.co.uk
https://twitter.com/vth_uk

We would like you to focus your efforts at designing the page in such a way so that it is very easy for visitor be open an account with the exchange. We must focus at informing the visitor about the bitcoin, how to my buy, how to sell, look at the general overview of the maker and CONVERTING him/her sing up. This is the most important!!

Regards,
Oren

Reason: Dear all, We are very keen on getting this design done right the first time. The key success is conversion of visitors to subscribers and then to traders. It is absolutely essential make the registration process as streamlined as possible! When we are calling them to act by "Change the world one bitcoin at a time" we should give them a opportunity to provide us with relevant account creation details: email, password, confirm password. Please visit quenzo.co.uk for ideas. Secondly, tell them what is a bitcoin, why a bitcoin is a good investment and how to invest. Finally, it is important to inform visitors of "who we are", what sets us apart from other exchanges, tell them about our experience. In our view graphs and live order books are important but they might turn some visitors away especially the ones that are not accustomed to online trading. Think of what would you like to see on the page if you wanted YOURSELF to invest. What would make you to create an account and use it? Think what will work, we are here to revolutionise how people do business.... any wild ideas put them to us. OUR BUDGET JUST GONE UP!!!

Target Market(s)

A combination of professional and consumer bitcoin investors.

Requirements
Must have
• News section

```html
<!DOCTYPE html>
<html lang="en">
<head>
<meta charset="utf-8">
<title>Velmora Trade Hall</title>
<link href="https://fonts.googleapis.com/css2?family=Arimo:wght@400;700&display=swap" rel="stylesheet">
<style>
:root{
  --blue:#0a94d2;
  --blue-dark:#0679b4;
  --blue-text:#1089cc;
  --tab-dark:#4a4a4a;
  --tab-darker:#3a3a3a;
  --text:#333;
  --muted:#666;
  --line:#e2e2e2;
  --row-hi:#d4ebf9;
  --head-light:#a9daf6;
  --orange:#f98c06;
  --white:#fff;
  --panel-bg:#f3f3f3;
}
*{box-sizing:border-box;margin:0;padding:0}
html,body{width:1200px;height:1200px;overflow:hidden;background:var(--white);font-family:"Arimo",Arial,sans-serif;color:var(--text);font-size:12px}
.abs{position:absolute}
.page{position:relative;width:1200px;height:1200px}

/* header */
.brand{left:30px;top:28px;display:flex;align-items:center;gap:12px}
.brand-dot{width:30px;height:30px;border-radius:50%;background:var(--blue)}
.brand-name{font-size:17px;color:#555;letter-spacing:1px}
.stat{top:24px;width:118px;height:52px;background:linear-gradient(#f6f6f6,#e6e6e6);border:1px solid #d6d6d6;padding:9px 0 0 17px;line-height:15px}
.stat .label{color:var(--blue-text);font-size:13px}
.stat .value{color:#555;font-size:13px;font-weight:700}
.login{left:841px;top:24px;width:333px;height:52px;background:linear-gradient(#22a6e2,var(--blue-dark));border-radius:4px 26px 26px 4px}
.login .field{top:12px;width:113px;height:26px;background:#fff;border:1px solid #c7e5f5}
.login .btn{left:268px;top:17px;color:#fff;font-weight:700;font-size:13px}

/* nav */
.nav{left:0;top:96px;width:1200px;height:40px;border-top:1px solid #ddd;background:#fff}
.nav .home{left:25px;top:0;width:97px;height:39px;background:linear-gradient(#2aa8e3,var(--blue-dark));color:#fff;font-weight:700;text-align:center;line-height:39px}
.nav .item{top:13px;color:var(--muted);font-weight:700}
.nav .sep{top:13px;color:#888}
.cta{left:871px;top:7px;width:176px;height:25px;border-radius:13px;background:linear-gradient(#ffa12a,var(--orange));color:#fff;font-weight:700;text-align:center;line-height:25px;border:1px solid #e07800}
.lang{left:1058px;top:7px;width:115px;height:25px;border-radius:13px;border:1px solid #bbb;background:linear-gradient(#fff,#eee);font-weight:700;color:#333;line-height:23px;padding-left:22px}
.lang svg{position:absolute;right:14px;top:8px}

.main{left:0;top:136px;width:1200px;height:940px;background:var(--blue)}
.panel{background:#fff;border-radius:4px;overflow:hidden}
.tab{top:0;height:30px;text-align:center;line-height:30px;font-weight:700;font-size:12px;color:#fff;background:linear-gradient(#555,var(--tab-darker))}
.tab.on{background:#fff;color:var(--blue-text)}

/* markets */
.market{left:0;width:245px;height:50px;border-bottom:1px solid var(--line)}
.market.hi{background:var(--row-hi)}
.market .star{left:12px;top:18px}
.market .pair{left:32px;top:19px;font-size:12px}
.market .spark{left:101px;top:14px;width:51px;height:22px;border:1px solid #d8e8f2;background:#fff}
.market .val{right:28px;top:19px;font-size:12px}
.market .arr{right:10px;top:20px}
.up{color:var(--blue-text)}
.down{color:var(--orange)}

/* tweets */
.tweets h3{left:19px;top:16px;font-size:15px;color:var(--blue-text)}
.follow{left:170px;top:12px;width:66px;height:21px;border:1px solid #ccc;background:linear-gradient(#fff,#e8e8e8);border-radius:3px;font-weight:700;font-size:11px;color:#333;text-align:center;line-height:19px}
.tweet-dot{width:14px;height:14px;border-radius:50%;background:var(--blue)}
.tweet .who{font-weight:700;font-size:12px}
.tweet .handle,.tweet .date{color:var(--muted);font-size:12px}
.tweet .body{font-size:12px;line-height:16px;color:#333}

/* chart */
.tf{left:18px;top:48px;display:flex;border:1px solid #999}
.tf span{padding:1px 3px;font-size:12px;border-right:1px solid #999;background:#f4f4f4}
.tf span.on{background:#9cd3e8}
.tf span:last-child{border-right:0}

/* orders */
.ohead{left:0;top:30px;width:560px;height:36px;background:var(--head-light);color:#444}
.ohead span,.orow span{position:absolute;top:0;line-height:36px}
.orow{left:0;width:560px;height:27px;border-bottom:1px solid var(--line)}
.orow span{line-height:27px}
.orow.hi{background:var(--row-hi)}

/* trade */
.form-label{left:22px;font-size:12px;color:#444}
.form-input{left:112px;width:165px;height:21px;border:1px solid #ccc;border-radius:2px;background:#fff}
.btn-blue{top:214px;width:124px;height:31px;border-radius:4px;background:linear-gradient(#22a6e2,var(--blue-dark));color:#fff;font-weight:700;text-align:center;line-height:31px}

/* book */
.bhead{left:0;top:0;height:37px;line-height:37px;text-align:center;color:#fff;font-weight:700;background:linear-gradient(#555,var(--tab-darker))}
.brow{left:0;width:301px;height:27px;border-bottom:1px solid var(--line)}
.brow span{position:absolute;top:0;line-height:27px;text-align:right}
.tint{position:absolute;top:0;height:26px;background:#e4f2fb}

/* footer */
.footer{left:0;top:1076px;width:1200px;height:40px;background:#fff;border-bottom:3px solid #e8e8e8;text-align:center;line-height:42px;font-weight:700;color:#444;font-size:12px}
.footer span{margin:0 12px}
.copy{left:0;top:1127px;width:1200px;text-align:center;font-size:11px;color:#444}
</style>
</head>
<body>
<div class="page">

  <header>
    <div class="abs brand"><span class="brand-dot"></span><span class="brand-name">Velmora Trade Hall</span></div>
    <div class="abs stat" style="left:357px"><div class="label">Last price</div><div class="value">503.122 USD</div></div>
    <div class="abs stat" style="left:478px"><div class="label">Low price</div><div class="value">472.3 USD</div></div>
    <div class="abs stat" style="left:598px"><div class="label">High price</div><div class="value">529.367 USD</div></div>
    <div class="abs stat" style="left:719px"><div class="label">Volume</div><div class="value">129.1 BTC</div></div>
    <div class="abs login">
      <div class="abs field" style="left:21px"></div>
      <div class="abs field" style="left:143px"></div>
      <div class="abs btn">LOGIN ➔</div>
    </div>
  </header>

  <nav class="abs nav">
    <div class="abs home">HOME</div>
    <span class="abs item" style="left:150px">BUY</span><span class="abs sep" style="left:202px">|</span>
    <span class="abs item" style="left:231px">SELL</span><span class="abs sep" style="left:289px">|</span>
    <span class="abs item" style="left:318px">OVERVIEW</span><span class="abs sep" style="left:410px">|</span>
    <span class="abs item" style="left:439px">WHO WE ARE</span><span class="abs sep" style="left:547px">|</span>
    <span class="abs item" style="left:576px">NEWS</span>
    <div class="abs cta">OPEN YOUR ACCOUNT</div>
    <div class="abs lang">ENGLISH<svg width="11" height="7"><path d="M0 0h11L5.5 7z" fill="#555"/></svg></div>
  </nav>

  <main class="abs main">

    <!-- markets -->
    <section class="abs panel" style="left:27px;top:16px;width:245px;height:377px">
      <div class="abs tab on" style="left:0;width:130px">ALL</div>
      <div class="abs tab" style="left:130px;width:115px">★ FAVS</div>
      <div class="abs" style="left:0;top:30px;width:245px;height:1px;background:#ccc"></div>
      <div class="abs market" style="top:38px"><span class="abs star down">★</span><span class="abs pair">LTC/USD</span><span class="abs spark"></span><span class="abs val up">13.8245</span><span class="abs arr up">▲</span></div>
      <div class="abs market hi" style="top:81px"><span class="abs star up">★</span><span class="abs pair">BTC/USD</span><span class="abs spark"></span><span class="abs val up">501.9990</span><span class="abs arr up">▲</span></div>
      <div class="abs market" style="top:130px"><span class="abs star down">★</span><span class="abs pair">EUR/USD</span><span class="abs spark"></span><span class="abs val down">1.3518</span><span class="abs arr down">▼</span></div>
      <div class="abs market" style="top:180px"><span class="abs star down">★</span><span class="abs pair">LTC/BTC</span><span class="abs spark"><svg width="49" height="20"><path d="M2 16h8l3-10h3l2 10 4-4h4l3 4h18" fill="none" stroke="#1089cc"/></svg></span><span class="abs val down">0.0277</span><span class="abs arr down">▼</span></div>
      <div class="abs market" style="top:230px"><span class="abs star down">★</span><span class="abs pair">BTC/EUR</span><span class="abs spark"></span><span class="abs val down">368.5100</span><span class="abs arr down">▼</span></div>
      <div class="abs market" style="top:280px"><span class="abs star down">★</span><span class="abs pair">LTC/EUR</span><span class="abs spark"></span><span class="abs val down">10.2840</span><span class="abs arr down">▼</span></div>
    </section>

    <!-- tweets -->
    <section class="abs panel tweets" style="left:27px;top:413px;width:245px;height:377px">
      <h3 class="abs">Tweets</h3>
      <div class="abs follow">Follow</div>
      <div class="abs" style="left:0;top:41px;width:245px;height:1px;background:var(--line)"></div>
      <div class="abs tweet" style="left:15px;top:58px;width:220px">
        <span class="abs tweet-dot" style="left:4px;top:8px"></span>
        <span class="abs who" style="left:36px;top:0">VTH</span>
        <span class="abs date" style="left:182px;top:1px">21 Mar</span>
        <span class="abs handle" style="left:36px;top:18px">@vth_uk</span>
        <p class="abs body" style="left:0;top:38px;width:210px">Velmora Trade Hall is a powerful and secure cryptocurrency trading platform designed for retail and institutional investors.</p>
        <span class="abs handle" style="left:0;top:106px">Expand</span>
      </div>
      <div class="abs" style="left:0;top:198px;width:245px;height:1px;background:var(--line)"></div>
      <div class="abs tweet" style="left:13px;top:213px;width:222px">
        <span class="abs tweet-dot" style="left:4px;top:8px"></span>
        <span class="abs who" style="left:36px;top:0">VTH</span>
        <span class="abs date" style="left:182px;top:1px">21 Mar</span>
        <span class="abs handle" style="left:36px;top:18px">@vth_uk</span>
        <p class="abs body" style="left:0;top:38px;width:200px">Change the world one bitcoin at a time.</p>
      </div>
      <div class="abs" style="left:0;top:299px;width:245px;height:1px;background:var(--line)"></div>
      <div class="abs" style="left:0;top:306px;width:232px;text-align:center;font-weight:700;color:var(--blue-text)">Load More</div>
    </section>

    <!-- chart -->
    <section class="abs panel" style="left:292px;top:16px;width:560px;height:379px">
      <div class="abs tab" style="left:0;width:140px">QUOTES</div>
      <div class="abs tab" style="left:140px;width:140px">CANDLES</div>
      <div class="abs tab" style="left:280px;width:140px">DEPTH</div>
      <div class="abs tab on" style="left:420px;width:140px">VOLUME</div>
      <div class="abs tf"><span>M1</span><span class="on">M5</span><span>M15</span><span>M30</span><span>H1</span><span>H4</span></div>
      <div class="abs" style="left:0;top:60px;width:562px;text-align:center;font-weight:700;font-size:13px;color:#333">BTC/USD</div>
      <svg class="abs" style="left:0;top:0" width="560" height="379" role="img" aria-label="BTC/USD traded volume bar chart">
        <g font-family="Arimo,Arial,sans-serif" font-size="12" fill="#333">
          <text x="13" y="175">5.5</text><text x="13" y="255">2.7</text>
          <text x="130" y="352">10:50</text><text x="214" y="352">11:40</text><text x="299" y="352">12:30</text><text x="385" y="352">13:20</text><text x="470" y="352">14:10</text>
        </g>
        <g stroke="#e8e8e8"><line x1="45" y1="174" x2="548" y2="174"/><line x1="45" y1="255" x2="548" y2="255"/><line x1="45" y1="333" x2="548" y2="333"/></g>
        <g fill="#0a94d2" transform="translate(-292 -152)">
          <rect x="350" y="482" width="7" height="3"/><rect x="358" y="483" width="7" height="2"/>
          <rect x="375" y="477" width="7" height="8"/><rect x="383" y="470" width="7" height="15"/><rect x="392" y="467" width="7" height="18"/>
          <rect x="401" y="393" width="7" height="92"/><rect x="409" y="464" width="7" height="21"/><rect x="417" y="452" width="7" height="33"/>
          <rect x="449" y="477" width="7" height="8"/><rect x="458" y="480" width="7" height="5"/><rect x="483" y="482" width="7" height="3"/>
          <rect x="509" y="479" width="7" height="6"/><rect x="518" y="480" width="7" height="5"/><rect x="526" y="482" width="6" height="3"/>
          <rect x="540" y="477" width="7" height="8"/><rect x="549" y="464" width="7" height="21"/><rect x="557" y="430" width="7" height="55"/>
          <rect x="575" y="440" width="7" height="45"/><rect x="592" y="470" width="7" height="15"/><rect x="601" y="448" width="7" height="37"/>
          <rect x="609" y="432" width="7" height="53"/><rect x="617" y="372" width="7" height="113"/>
          <rect x="669" y="481" width="7" height="4"/><rect x="685" y="479" width="7" height="6"/><rect x="700" y="244" width="7" height="241"/>
          <rect x="727" y="481" width="7" height="4"/><rect x="735" y="380" width="7" height="105"/>
          <rect x="751" y="473" width="7" height="12"/><rect x="759" y="473" width="7" height="12"/>
          <rect x="801" y="395" width="7" height="90"/><rect x="809" y="440" width="7" height="45"/><rect x="818" y="475" width="7" height="10"/><rect x="834" y="473" width="7" height="12"/>
        </g>
      </svg>
    </section>

    <!-- orders -->
    <section class="abs panel" style="left:292px;top:413px;width:560px;height:501px">
      <div class="abs tab" style="left:0;width:179px">ACTIVE ORDERS</div>
      <div class="abs tab" style="left:181px;width:198px;background:linear-gradient(#22a6e2,var(--blue-dark))">ALL ORDERS</div>
      <div class="abs tab" style="left:381px;width:179px">TRADE HISTORY</div>
      <div class="abs ohead">
        <span style="left:23px">Market</span><span style="left:102px">Time</span><span style="left:235px">Type</span><span style="left:305px">Volume(BTC)</span><span style="left:413px">Price</span><span style="left:481px">Total(USD)</span>
      </div>
      <div class="abs" style="left:0;top:68px;width:560px">
        <div class="abs orow" style="top:0"><span style="left:23px">LTC/USD</span><span style="left:102px">29 Mar 2014 19:59:54</span><span style="left:239px">Sell</span><span style="left:308px">0.61098</span><span style="left:411px">13.78011</span><span style="left:491px">8.4194</span></div>
        <div class="abs orow" style="top:27px"><span style="left:23px">LTC/USD</span><span style="left:102px">29 Mar 2014 19:59:54</span><span style="left:239px">Sell</span><span style="left:308px">0.61098</span><span style="left:411px">13.78011</span><span style="left:491px">8.4194</span></div>
        <div class="abs orow" style="top:54px"><span style="left:23px">LTC/USD</span><span style="left:102px">29 Mar 2014 19:59:54</span><span style="left:239px">Sell</span><span style="left:308px">0.61098</span><span style="left:411px">13.78011</span><span style="left:491px">8.4194</span></div>
        <div class="abs orow" style="top:81px"><span style="left:23px">LTC/USD</span><span style="left:102px">29 Mar 2014 19:59:54</span><span style="left:239px">Sell</span><span style="left:308px">0.61098</span><span style="left:411px">13.78011</span><span style="left:491px">8.4194</span></div>
        <div class="abs orow" style="top:108px"><span style="left:23px">LTC/USD</span><span style="left:102px">29 Mar 2014 19:59:54</span><span style="left:239px">Sell</span><span style="left:308px">0.61098</span><span style="left:411px">13.78011</span><span style="left:491px">8.4194</span></div>
        <div class="abs orow hi" style="top:135px"><span style="left:23px">LTC/USD</span><span style="left:102px">29 Mar 2014 19:59:54</span><span style="left:239px">Sell</span><span style="left:308px">0.61098</span><span style="left:411px">13.78011</span><span style="left:491px">8.4194</span></div>
        <div class="abs orow" style="top:162px"><span style="left:23px">LTC/USD</span><span style="left:102px">29 Mar 2014 19:59:54</span><span style="left:239px">Sell</span><span style="left:308px">0.61098</span><span style="left:411px">13.78011</span><span style="left:491px">8.4194</span></div>
        <div class="abs orow" style="top:189px"><span style="left:23px">LTC/USD</span><span style="left:102px">29 Mar 2014 19:59:54</span><span style="left:239px">Sell</span><span style="left:308px">0.61098</span><span style="left:411px">13.78011</span><span style="left:491px">8.4194</span></div>
        <div class="abs orow" style="top:216px"><span style="left:23px">LTC/USD</span><span style="left:102px">29 Mar 2014 19:59:54</span><span style="left:239px">Sell</span><span style="left:308px">0.61098</span><span style="left:411px">13.78011</span><span style="left:491px">8.4194</span></div>
        <div class="abs orow" style="top:243px"><span style="left:23px">LTC/USD</span><span style="left:102px">29 Mar 2014 19:59:54</span><span style="left:239px">Sell</span><span style="left:308px">0.61098</span><span style="left:411px">13.78011</span><span style="left:491px">8.4194</span></div>
        <div class="abs orow" style="top:270px"><span style="left:23px">LTC/USD</span><span style="left:102px">29 Mar 2014 19:59:54</span><span style="left:239px">Sell</span><span style="left:308px">0.61098</span><span style="left:411px">13.78011</span><span style="left:491px">8.4194</span></div>
        <div class="abs orow" style="top:297px"><span style="left:23px">LTC/USD</span><span style="left:102px">29 Mar 2014 19:59:54</span><span style="left:239px">Sell</span><span style="left:308px">0.61098</span><span style="left:411px">13.78011</span><span style="left:491px">8.4194</span></div>
        <div class="abs orow" style="top:324px"><span style="left:23px">LTC/USD</span><span style="left:102px">29 Mar 2014 19:59:54</span><span style="left:239px">Sell</span><span style="left:308px">0.61098</span><span style="left:411px">13.78011</span><span style="left:491px">8.4194</span></div>
        <div class="abs orow" style="top:351px"><span style="left:23px">LTC/USD</span><span style="left:102px">29 Mar 2014 19:59:54</span><span style="left:239px">Sell</span><span style="left:308px">0.61098</span><span style="left:411px">13.78011</span><span style="left:491px">8.4194</span></div>
        <div class="abs orow" style="top:378px"></div>
      </div>
    </section>

    <!-- trade form -->
    <section class="abs panel" style="left:873px;top:16px;width:301px;height:287px">
      <div class="abs" style="left:0;top:0;width:160px;height:41px;text-align:center;padding-top:8px;line-height:14px;color:var(--blue-text)"><b>BUY LTC</b><br>13,79989 USD</div>
      <div class="abs" style="left:160px;top:0;width:141px;height:41px;text-align:center;padding-top:8px;line-height:14px;color:#fff;background:linear-gradient(#555,var(--tab-darker))"><b>SELL LTC</b><br>13,76545 USD</div>
      <span class="abs form-label" style="top:68px">Type</span>
      <div class="abs form-input" style="top:64px;padding:3px 10px;font-size:12px">Limit<svg style="position:absolute;right:2px;top:2px" width="15" height="15"><rect x=".5" y=".5" width="14" height="14" fill="#eee" stroke="#888"/><path d="M4 6h7l-3.5 4z" fill="#222"/></svg></div>
      <span class="abs form-label" style="top:96px">Volume LTC</span><div class="abs form-input" style="top:92px"></div>
      <span class="abs form-label" style="top:124px">Price per LTC</span><div class="abs form-input" style="top:118px"></div>
      <span class="abs form-label" style="top:152px">Total</span><span class="abs form-label" style="left:123px;top:153px">Fee</span>
      <span class="abs form-label" style="top:180px">USD 0.0000</span><span class="abs form-label" style="left:123px;top:181px">LTC 0.00000</span>
      <div class="abs btn-blue" style="left:22px">BUY LTC</div>
      <div class="abs btn-blue" style="left:152px">CANCEL</div>
      <div class="abs" style="left:0;top:252px;width:297px;text-align:center;font-size:11px;color:#444">Commission for the transaction is 0.2%</div>
    </section>

    <!-- order book -->
    <section class="abs panel" style="left:873px;top:324px;width:301px;height:528px">
      <div class="abs bhead" style="width:102px">BID</div>
      <div class="abs bhead" style="left:103px;width:95px">PRICE</div>
      <div class="abs bhead" style="left:199px;width:102px">ASK</div>
      <div class="abs" style="left:0;top:39px;width:301px">
        <div class="abs brow" style="top:0"><i class="tint" style="left:0;width:102px"></i><span style="left:103px;width:77px">13.87000</span><span style="left:199px;width:88px">8.38509</span></div>
        <div class="abs brow" style="top:27px"><i class="tint" style="left:0;width:102px"></i><span style="left:103px;width:77px">13.86900</span><span style="left:199px;width:88px">0.04082</span></div>
        <div class="abs brow" style="top:54px"><i class="tint" style="left:0;width:102px"></i><span style="left:103px;width:77px">13.86700</span><span style="left:199px;width:88px">37.93103</span></div>
        <div class="abs brow" style="top:81px"><i class="tint" style="left:0;width:102px"></i><span style="left:103px;width:77px">13.866909</span><span style="left:199px;width:88px">9.91035</span></div>
        <div class="abs brow" style="top:108px"><i class="tint" style="left:0;width:102px"></i><span style="left:103px;width:77px">13.86000</span><span style="left:199px;width:88px">8.83279</span></div>
        <div class="abs brow" style="top:135px"><i class="tint" style="left:0;width:102px"></i><span style="left:103px;width:77px">13.85990</span><span style="left:199px;width:88px">3.03464</span></div>
        <div class="abs brow" style="top:162px"><i class="tint" style="left:0;width:102px"></i><span style="left:103px;width:77px">13.85800</span><span style="left:199px;width:88px">58.47953</span></div>
        <div class="abs brow" style="top:189px"><i class="tint" style="left:0;width:102px"></i><span style="left:103px;width:77px">13.83764</span><span style="left:199px;width:88px">0.51282</span></div>
        <div class="abs brow" style="top:216px"><i class="tint" style="left:0;width:102px"></i><span style="left:103px;width:77px">13.80100</span><span style="left:199px;width:88px">9.25926</span></div>
        <div class="abs brow" style="top:243px"><i class="tint" style="left:0;width:102px"></i><span style="left:103px;width:77px">13.800002</span><span style="left:199px;width:88px">.00933</span></div>
        <div class="abs brow" style="top:270px"><i class="tint" style="left:199px;width:102px"></i><span style="left:0;width:88px">53.76344</span><span style="left:103px;width:77px">13.76344</span></div>
        <div class="abs brow" style="top:297px"><i class="tint" style="left:199px;width:102px"></i><span style="left:0;width:88px">44.44444</span><span style="left:103px;width:77px">13.75100</span></div>
        <div class="abs brow" style="top:324px"><i class="tint" style="left:199px;width:102px"></i><span style="left:0;width:88px">0.26455</span><span style="left:103px;width:77px">13.75000</span></div>
        <div class="abs brow" style="top:351px"><i class="tint" style="left:199px;width:102px"></i><span style="left:0;width:88px">25.22936</span><span style="left:103px;width:77px">13.73800</span></div>
        <div class="abs brow" style="top:378px"><i class="tint" style="left:199px;width:102px"></i><span style="left:0;width:88px">0.06098</span><span style="left:103px;width:77px">13.73000</span></div>
        <div class="abs brow" style="top:405px"><i class="tint" style="left:199px;width:102px"></i><span style="left:0;width:88px">0.04016</span><span style="left:103px;width:77px">13.72100</span></div>
        <div class="abs brow" style="top:432px"><i class="tint" style="left:199px;width:102px"></i><span style="left:0;width:88px">14.88372</span><span style="left:103px;width:77px">13.72000</span></div>
        <div class="abs brow" style="top:459px;border-bottom:0"><i class="tint" style="left:199px;width:102px"></i><span style="left:0;width:88px">0.57921</span><span style="left:103px;width:77px">13.71024</span></div>
      </div>
    </section>

  </main>

  <footer class="abs footer">
    <span>HOME</span>|<span>API TRADE</span>|<span>TERMS AND CONDITIONS</span>|<span>CONTACTS</span>|<span>SUPPORT</span>
  </footer>
  <div class="abs copy">© 2014 Velmora Trade Hall Limited. All rights reserved</div>
</div>
</body>
</html>
```